Multi-Faceted Legal and Finanacial Advisory Group Needs Business Card Design

We need a business card design for a newly branded Orlando Florida area advising group consisting of Attorneys, Accountants and Financial Planners. The company is named RT Counsel Group. You will find our initial work on a business card. The information on the business card are merely guideposts and not final product. The logo does not have the be the same as provided since we have not finalized the logo. We would like to stay with a black/white/grey color scheme, but limited use of color is not out of the question.

Target Market(s)

Businesses and their Corporate Representatives

Industry/Entity Type

Business

Contact Information for Business Card

Should have Name, Title, Phone, Cell, Fax, Email and website. Logo should incorporate RT in some fashion however final logo used does not have to be the one on the document provided.

Requirements
Must have
• An RT design on front and back.

```html
<!DOCTYPE html>
<html lang="en">
<head>
<meta charset="utf-8">
<title>RT Counsel Group – Business Card Options</title>
<link href="https://fonts.googleapis.com/css2?family=Alegreya+Sans:ital,wght@0,400;0,500;1,400&display=swap" rel="stylesheet">
<style>
  :root {
    --stage: #000000;
    --front-mid: #6a6a6a;
    --front-edge: #3a3a3a;
    --back-mid: #d6d6d6;
    --back-edge: #a9a9a9;
    --panel: #cfcfcf;
    --ink-light: #f2f2f2;
    --ink-dark: #1e1e1e;
    --mark-grey: #8a8a8a;
    --mark-blue: #134a94;
    --label: #ffffff;
  }
  * { box-sizing: border-box; margin: 0; padding: 0; }
  html, body { width: 1200px; height: 884px; overflow: hidden; background: var(--stage); }
  body { position: relative; font-family: "Alegreya Sans", sans-serif; }

  .card {
    position: absolute;
    width: 525px;
    height: 300px;
  }
  .card--front { background: radial-gradient(ellipse at 50% 40%, var(--front-mid) 0%, var(--front-edge) 100%); top: 111px; }
  .card--back  { background: radial-gradient(ellipse at 50% 45%, var(--back-mid) 0%, var(--back-edge) 100%); top: 481px; }
  .option-grey { left: 48px; }
  .option-blue { left: 624px; }

  .brand-panel {
    position: absolute;
    left: 34px; top: 53px;
    width: 191px; height: 191px;
    background: var(--panel);
    display: flex; align-items: center; justify-content: center;
    text-align: center;
  }
  .brand-name {
    font-weight: 500;
    text-transform: uppercase;
    line-height: 1.05;
  }
  .brand-panel .brand-name { font-size: 27px; letter-spacing: 1px; }
  .option-grey .brand-name { color: var(--mark-grey); }
  .option-blue .brand-name { color: var(--mark-blue); }

  .contact {
    position: absolute;
    left: 251px; top: 58px;
    color: var(--ink-light);
    font-size: 14.5px;
    line-height: 20px;
  }
  .contact .person { font-size: 21px; font-weight: 500; line-height: 26px; }
  .contact .title { font-style: italic; font-size: 16px; margin-bottom: 12px; }

  .card--back .brand-name {
    position: absolute;
    left: 0; right: 0; top: 190px;
    text-align: center;
    font-size: 34px;
    letter-spacing: 1px;
  }
  .services {
    position: absolute;
    left: 0; right: 0; top: 236px;
    text-align: center;
    color: var(--ink-dark);
    font-size: 16px;
    letter-spacing: 2.6px;
  }

  .side-label {
    position: absolute;
    width: 525px;
    text-align: center;
    color: var(--label);
    font-size: 21px;
    font-weight: 500;
    letter-spacing: 1px;
  }
  .side-label--front { top: 428px; }
  .side-label--back { top: 798px; }
</style>
</head>
<body>
  <!-- Grey option -->
  <section class="card card--front option-grey">
    <div class="brand-panel"><span class="brand-name">RT<br>Counsel Group</span></div>
    <div class="contact">
      <p class="person">DANIEL K. AVERY, Esq.</p>
      <p class="title">Attorney</p>
      <p>2200 Harbor Point Drive, Suite 410</p>
      <p>Cedar Hollow, FL 32000</p>
      <p>Office: (555) 010-2040</p>
      <p>Cell: (555) 010-2041</p>
      <p>Email: davery@rt-counsel.com</p>
      <p>www.rt-counsel.com</p>
    </div>
  </section>
  <p class="side-label side-label--front option-grey">FRONT</p>

  <section class="card card--back option-grey">
    <span class="brand-name">RT Counsel Group</span>
    <p class="services">Attorneys • Accountants • Financial Planners</p>
  </section>
  <p class="side-label side-label--back option-grey">BACK</p>

  <!-- Blue accent option -->
  <section class="card card--front option-blue">
    <div class="brand-panel"><span class="brand-name">RT<br>Counsel Group</span></div>
    <div class="contact">
      <p class="person">DANIEL K. AVERY, Esq.</p>
      <p class="title">Attorney</p>
      <p>2200 Harbor Point Drive, Suite 410</p>
      <p>Cedar Hollow, FL 32000</p>
      <p>Office: (555) 010-2040</p>
      <p>Cell: (555) 010-2041</p>
      <p>Email: davery@rt-counsel.com</p>
      <p>www.rt-counsel.com</p>
    </div>
  </section>
  <p class="side-label side-label--front option-blue">FRONT</p>

  <section class="card card--back option-blue">
    <span class="brand-name">RT Counsel Group</span>
    <p class="services">Attorneys • Accountants • Financial Planners</p>
  </section>
  <p class="side-label side-label--back option-blue">BACK</p>
</body>
</html>
```